Need 4 Page Brush Catalogue Redesign ASAP i will sellect any one.

I have attached my existing design please do the redesign with best look.

We are an industrial brush distributor in Texas. We provide high grade brushes to the rubber, metalwork, welding/pipeline, automotive, aerospace and other industries. So, if you are looking for one of the top-rated brass wire brushes suppliers, a wire wheel brush supplier, or any other kind of brush supplier in Texas, make us your choice!

Our brushes are manufactured using high quality raw materials and are appreciated for corrosion resistance, accurate dimensions, easy installation, smooth finish, long service life and sturdy design. The best part about our brushes is that they are stringently tested by our quality controller on different parameters.

Quarn Bristle has a reputation for flexibility, innovation and the ability to react to the needs of customers quickly. Having about 25 years of experience in this industry gives us an insight into the objectives and challenges of different projects and the ability of recommending the best solution for your application.

Get in touch with us today for finding out how we can help you with brush supplies for your business.
please check the link http://www.quarnbristle.example/

DON'T CALL
Updates

Please use attached logo at your design. Added Monday, June 12, 2017

Target Market(s)

brush industry reseller

Industry/Entity Type

Industrial

Font styles to use
Serif
Sans Serif

Colors

Designer to choose colors to be used in the design.

Requirements
Must have
• creative and i catchy
Nice to have
• must be creative
Should not have
• don't use clip art

```html
<!DOCTYPE html>
<html lang="en">
<head>
<meta charset="utf-8">
<title>Quarn Bristle Catalogue Cover</title>
<link rel="stylesheet" href="https://fonts.googleapis.com/css2?family=Russo+One&display=swap">
<style>
  :root {
    --backdrop: #3a3a3c;
    --paper: #ffffff;
    --sky: #9fd4ef;
    --sky-pale: #d6eef9;
    --ocean: #1e88d0;
    --ocean-deep: #1a5aa6;
    --ink: #1d1d1f;
    --logo-font: "Russo One", sans-serif;
  }
  html, body {
    margin: 0;
    width: 1200px;
    height: 800px;
    overflow: hidden;
    background: var(--backdrop);
  }
  .spread {
    position: absolute;
    left: 80px;
    top: 50px;
    width: 1040px;
    height: 700px;
    display: flex;
    box-shadow: 0 12px 40px rgba(0,0,0,.45);
  }
  .page {
    position: relative;
    width: 520px;
    height: 700px;
    background: var(--paper);
    overflow: hidden;
  }
  .page svg { position: absolute; inset: 0; width: 100%; height: 100%; }
  .brand-name {
    position: absolute;
    margin: 0;
    font-family: var(--logo-font);
    font-weight: 400;
    color: var(--ink);
    letter-spacing: .5px;
    white-space: nowrap;
  }
  .back-cover .brand-name { right: 40px; top: 80px; font-size: 34px; }
  .front-cover .brand-name { left: 60px; top: 78px; font-size: 44px; }
  .web-address {
    position: absolute;
    margin: 0;
    font-family: var(--logo-font);
    font-weight: 400;
    letter-spacing: 1.5px;
    white-space: nowrap;
  }
  .back-cover .web-address { left: 80px; bottom: 48px; font-size: 15px; color: var(--ink); }
  .front-cover .web-address { left: 0; right: 0; text-align: center; bottom: 60px; font-size: 16px; color: var(--paper); }
</style>
</head>
<body>
<main class="spread">

  <section class="page back-cover">
    <svg viewBox="0 0 520 700">
      <defs>
        <linearGradient id="tube-brush-tones" x1="0" y1="0" x2="1" y2="1">
          <stop offset="0" stop-color="#7d7d80"/>
          <stop offset=".55" stop-color="#a27a3a"/>
          <stop offset="1" stop-color="#4a4a4e"/>
        </linearGradient>
      </defs>
      <path class="band-pale" d="M0,140 Q260,40 520,0 L520,130 Q300,170 0,320 Z" fill="var(--sky-pale)"/>
      <path class="band-sky" d="M0,200 Q280,90 520,60 L520,360 Q290,420 0,590 Z" fill="var(--sky)"/>
      <path class="band-white" d="M130,330 Q330,150 520,120 L520,360 Q380,300 130,330 Z" fill="var(--paper)"/>
      <path class="band-ocean" d="M0,380 Q200,520 420,380 L520,360 Q300,470 0,600 Z" fill="var(--ocean)"/>
      <g role="img" aria-label="Photo of twisted-wire tube brushes in steel and brass">
        <rect x="40" y="260" width="280" height="230" rx="18" fill="url(#tube-brush-tones)"/>
      </g>
    </svg>
    <h2 class="brand-name">QUARN BRISTLE</h2>
    <p class="web-address">WWW.QUARNBRISTLE.EXAMPLE</p>
  </section>

  <section class="page front-cover">
    <svg viewBox="0 0 520 700">
      <defs>
        <linearGradient id="ocean-fill" x1="0" y1="0" x2="1" y2="1">
          <stop offset="0" stop-color="var(--ocean)"/>
          <stop offset="1" stop-color="var(--ocean-deep)"/>
        </linearGradient>
        <linearGradient id="wheel-brush-tones" x1="0" y1="0" x2="1" y2="1">
          <stop offset="0" stop-color="#e2d3a0"/>
          <stop offset=".5" stop-color="#8a8a8c"/>
          <stop offset="1" stop-color="#3c3f42"/>
        </linearGradient>
      </defs>
      <path class="band-ocean" d="M0,330 Q240,210 520,170 L520,700 L0,700 Z" fill="url(#ocean-fill)"/>
      <path class="band-light" d="M0,400 L180,700 L0,700 Z" fill="var(--sky)" opacity=".35"/>
      <path class="band-light" d="M0,340 Q200,250 520,215 L520,250 Q240,290 0,400 Z" fill="var(--paper)" opacity=".18"/>
      <g role="img" aria-label="Photo of industrial wheel brushes in tampico, steel wire and nylon">
        <rect x="30" y="190" width="470" height="300" rx="30" fill="url(#wheel-brush-tones)"/>
      </g>
    </svg>
    <h1 class="brand-name">QUARN BRISTLE</h1>
    <p class="web-address">WWW.QUARNBRISTLE.EXAMPLE</p>
  </section>

</main>
</body>
</html>
```